Virtual Assistant/Online Marketing Business Card/Stationary

I need a professional but modern business card/stationary for my company in Dallas called Brivolo. Brivolo is a virtual assistant specializing in online marketing. I would like a unique design that stands out and makes my brand clear. Incorporating the logo is a must and have attached it to this brief.

Target Market(s)

small business owners & entrepreneurs, 35-65

Industry/Entity Type

Business

Contact Information for Business Card

Maren Tolk
marentolk@brivolo.biz
(555) 271-9064
brivolo.biz

Font styles to use
Sans Serif

Colors
f04a50
3176b5
9bcb3c

Requirements
Must have
• Colors that match the logo colors. Logo integration

```html
<!DOCTYPE html>
<html lang="en">
<head>
<meta charset="utf-8">
<title>Brivolo Business Card</title>
<link rel="stylesheet" href="https://fonts.googleapis.com/css2?family=Montserrat:wght@700;800&family=Quicksand:wght@400;500&display=swap">
<style>
  :root {
    --canvas: #e3e3e3;
    --paper: #ececec;
    --red: #d03a26;
    --ink: #282624;
    --white: #ffffff;
  }
  * { margin: 0; padding: 0; box-sizing: border-box; }
  html, body { width: 1200px; height: 900px; overflow: hidden; background: var(--canvas); }
  .canvas { position: relative; width: 1200px; height: 900px; }
  .card {
    position: absolute; left: 280px; width: 640px; height: 366px;
    background: var(--paper); overflow: hidden;
    box-shadow: 0 2px 6px rgba(0,0,0,.12);
  }
  .card--front { top: 54px; }
  .card--back { top: 480px; }
  .card__shapes { position: absolute; inset: 0; width: 100%; height: 100%; }
  .shape--red { fill: var(--red); }
  .shape--ink { fill: var(--ink); }
  .brand {
    position: absolute; left: 58px; top: 150px;
    display: flex; align-items: center; gap: 14px;
    font-family: "Montserrat", sans-serif; font-weight: 800;
    font-size: 58px; letter-spacing: -1px; color: var(--ink);
  }
  .brand__dot { width: 22px; height: 22px; border-radius: 50%; background: var(--red); }
  .name {
    position: absolute; right: 46px; top: 40px;
    font-family: "Montserrat", sans-serif; font-weight: 700;
    font-size: 20px; letter-spacing: .5px; color: var(--ink);
  }
  .name__last { color: var(--white); }
  .contact {
    position: absolute; right: 34px; top: 190px;
    list-style: none; text-align: right;
    font-family: "Quicksand", sans-serif; font-weight: 500;
    font-size: 14px; color: var(--white); line-height: 24px;
  }
  .contact__item { display: flex; justify-content: flex-end; align-items: center; gap: 8px; }
  .contact__icon {
    width: 15px; height: 15px; border-radius: 50%;
    border: 1.5px solid var(--red); display: inline-flex;
    align-items: center; justify-content: center;
  }
  .contact__icon svg { width: 8px; height: 8px; fill: var(--white); }
</style>
</head>
<body>
<main class="canvas">
  <section class="card card--front">
    <svg class="card__shapes" viewBox="0 0 700 400" preserveAspectRatio="none" aria-hidden="true">
      <path class="shape--red" d="M150,0 H700 V300 H520 V140 C390,60 270,30 150,0 Z"/>
      <path class="shape--ink" d="M0,335 C180,322 330,262 430,170 C500,105 570,80 700,75 V400 H0 Z"/>
    </svg>
    <div class="brand"><span class="brand__dot"></span>Brivolo</div>
  </section>

  <section class="card card--back">
    <svg class="card__shapes" viewBox="0 0 700 400" preserveAspectRatio="none" aria-hidden="true">
      <path class="shape--red" d="M150,0 H700 V300 H520 V140 C390,60 270,30 150,0 Z"/>
      <path class="shape--ink" d="M0,335 C180,322 330,262 430,170 C500,105 570,80 700,75 V400 H0 Z"/>
    </svg>
    <div class="brand"><span class="brand__dot"></span>Brivolo</div>
    <h1 class="name">MAREN <span class="name__last">TOLK</span></h1>
    <ul class="contact">
      <li class="contact__item">(555) 271-9064
        <span class="contact__icon"><svg viewBox="0 0 10 10"><path d="M2 0h2l1 2.5-1.3 1a6 6 0 0 0 2.8 2.8l1-1.3L10 6v2a2 2 0 0 1-2 2A8 8 0 0 1 0 2a2 2 0 0 1 2-2z"/></svg></span>
      </li>
      <li class="contact__item">marentolk@brivolo.biz
        <span class="contact__icon"><svg viewBox="0 0 10 10"><path d="M0 2h10v6H0z M0 2l5 3.5L10 2" /></svg></span>
      </li>
      <li class="contact__item">brivolo.biz
        <span class="contact__icon"><svg viewBox="0 0 10 10"><circle cx="5" cy="5" r="5"/></svg></span>
      </li>
    </ul>
  </section>
</main>
</body>
</html>
```